Company or website name
- StepTrova
- Links to the website
- www.steptrova.com
- Describe your company and organization and target audience
- Dance Class finder website  Primary target audience : Dance enthusiasts Goal: To allow dance enthusiasts to search for dance classes and studios in their immediate area that offers the dance classes they desire at specific time and days w/o having to deal with the hassle of searching through every studio's dance schedule  Secondary target audience: Dance Instructors Goal: To allow dance instructors to network with studios, create a following of dance students, educate the public on the classes they instruct (ie. What class, when, where, etc...).  Tertiary target audience: Dance Studios Goal: To give dance studios organizational tools that will allow them to manage their business and schedule better.
- The design should have the following
- Colors: Red, grey, purple  Logo: Silhouette of dancers in movement practicing different forms of dance. Logo will be background to "StepTrova" lettering.  "StepTrova" lettering: Letters placed together without spacing or adding characters in place of letters. I would like this to "Pop"
- Other Facts

```html
<!DOCTYPE html>
<html lang="en">
<head>
<meta charset="utf-8">
<title>StepTrova – Find Dance Classes Near You</title>
<link rel="stylesheet" href="https://fonts.googleapis.com/css2?family=Montserrat:wght@800;900&family=Kanit:wght@300;400&family=Source+Sans+3:wght@400;600;700&family=Arimo:wght@400;700&display=swap">
<style>
:root{
  --purple:#7b0c7e;
  --purple-dark:#5e0761;
  --yellow:#f3cf1c;
  --blue:#3f5f95;
  --hero-light:#ececec;
  --hero-mid:#dedede;
  --ink:#222;
  --muted:#8a8a8a;
  --line:#e3e3e3;
  --footer:#f3f3f3;
  --footer-bar:#e7e7e7;
  --white:#fff;
}
*{margin:0;padding:0;box-sizing:border-box}
html,body{width:1200px;height:2535px;overflow:hidden;background:var(--white)}
body{position:relative;font-family:"Source Sans 3",sans-serif;color:var(--ink)}

/* header */
.site-header{position:absolute;left:0;top:0;width:1200px;height:83px;background:var(--purple)}
.brand{position:absolute;left:235px;top:22px;font-family:"Source Sans 3",sans-serif;font-weight:700;font-size:30px;color:var(--white);letter-spacing:.5px}
.topbar{position:absolute;right:233px;top:9px;display:flex;gap:20px;font-size:9px;color:var(--white);align-items:center}
.topbar span{display:flex;align-items:center;gap:4px}
.social{position:absolute;right:233px;top:34px;display:flex;gap:8px}
.social i{width:8px;height:8px;border-radius:50%;background:#c9a3ca;display:block}
.main-nav{position:absolute;right:233px;top:62px;display:flex;gap:17px;font-size:9.5px;color:var(--white);letter-spacing:.2px}
.main-nav a{color:var(--white);text-decoration:none;position:relative}
.main-nav a.active{color:var(--yellow)}
.main-nav a.active::after{content:"";position:absolute;left:0;right:0;bottom:-5px;height:2px;background:var(--yellow)}

/* hero */
.hero{position:absolute;left:0;top:83px;width:1200px;height:410px}
.hero-art{position:absolute;inset:0;background:linear-gradient(180deg,var(--hero-light),var(--hero-mid))}
.hero-title{position:absolute;left:234px;top:118px;font-family:"Montserrat",sans-serif;font-weight:900;font-size:37px;line-height:34px;color:var(--purple);letter-spacing:.5px}
.hero-rule{position:absolute;left:235px;top:203px;width:29px;height:3px;background:var(--white)}
.hero-sub{position:absolute;left:235px;top:219px;font-family:"Arimo",sans-serif;font-size:14px;color:#111}
.search{position:absolute;left:235px;top:261px;width:240px;height:32px;background:var(--white);border:1px solid #ddd;display:flex;align-items:center;justify-content:space-between;padding:0 12px;font-family:"Arimo",sans-serif;font-size:8.5px;color:#222;letter-spacing:.2px}

/* section titles */
.section-title{position:absolute;left:0;width:1200px;text-align:center;font-family:"Kanit",sans-serif;font-weight:300;font-size:23px;color:var(--purple)}
.section-rule{position:absolute;left:585px;width:29px;height:2px;background:#d0d0d0}

/* instructor cards */
.instructor{position:absolute;top:635px;width:171px;height:276px;background:var(--white);border:1px solid #ececec;box-shadow:0 2px 3px rgba(0,0,0,.12)}
.instructor.featured{box-shadow:0 5px 8px rgba(0,0,0,.25)}
.avatar{position:absolute;left:18px;top:19px;width:42px;height:42px;background:linear-gradient(135deg,#8a6a55,#4b3a30)}
.instructor h3{position:absolute;left:17px;top:74px;font-family:"Kanit",sans-serif;font-weight:400;font-size:13.5px;color:var(--purple)}
.instructor .rule{position:absolute;left:18px;top:101px;width:24px;height:1px;background:#ccc}
.instructor p{position:absolute;left:17px;top:114px;width:140px;font-size:9.5px;line-height:13.2px;color:var(--muted)}
.instructor .divider{position:absolute;left:17px;right:17px;top:238px;height:1px;background:var(--line)}
.instructor a{position:absolute;left:19px;top:250px;font-size:10px;font-weight:600;color:#777;text-decoration:none}
.instructor.featured a{color:var(--purple);font-weight:700}

/* about */
.about-art{position:absolute;left:0;top:985px;width:600px;height:380px;background:linear-gradient(180deg,#d9d7d2 0%,#b9c9cf 40%,#b98a5a 85%,#9c6e43 100%)}
.about-panel{position:absolute;left:600px;top:985px;width:600px;height:380px;background:var(--purple)}
.about-title{position:absolute;left:35px;top:62px;font-family:"Montserrat",sans-serif;font-weight:900;font-size:34px;line-height:33px;color:var(--white)}
.about-title span{color:var(--yellow)}
.about-rule{position:absolute;left:35px;top:144px;width:29px;height:3px;background:var(--yellow)}
.about-text{position:absolute;left:35px;top:164px;width:330px;font-family:"Arimo",sans-serif;font-size:9.5px;line-height:13.2px;color:var(--white)}
.btn-outline{position:absolute;left:35px;top:285px;width:90px;height:32px;border:1px solid var(--yellow);color:var(--yellow);font-family:"Arimo",sans-serif;font-weight:700;font-size:8.5px;display:flex;align-items:center;justify-content:center}

/* studios */
.studio{position:absolute;width:232px;height:111px;background:var(--white);border:1px solid #e6e6e6}
.studio.featured{box-shadow:0 3px 5px rgba(0,0,0,.2)}
.studio-photo{position:absolute;left:0;top:0;width:100px;height:100%;background:linear-gradient(160deg,#6b5f8c,#3560a8 55%,#b8d23c)}
.studio h3{position:absolute;left:111px;top:14px;font-family:"Kanit",sans-serif;font-weight:400;font-size:13px;color:var(--purple)}
.studio .rule{position:absolute;left:111px;top:40px;width:20px;height:1px;background:#ccc}
.studio p{position:absolute;left:111px;top:50px;width:112px;font-size:8.6px;line-height:12px;color:var(--muted)}

/* promo band */
.promo{position:absolute;left:0;top:1816px;width:1200px;height:391px}
.promo-art{position:absolute;inset:0;background:var(--blue)}
.promo-kicker{position:absolute;left:0;width:1200px;top:98px;text-align:center;font-family:"Kanit",sans-serif;font-weight:300;font-size:17px;color:var(--yellow)}
.promo-title{position:absolute;left:0;width:1200px;top:120px;text-align:center;font-family:"Montserrat",sans-serif;font-weight:900;font-size:30px;color:var(--yellow);letter-spacing:.5px}
.promo-rule{position:absolute;left:586px;top:170px;width:29px;height:3px;background:var(--white)}
.promo-text{position:absolute;left:290px;width:620px;top:190px;text-align:center;font-family:"Arimo",sans-serif;font-size:9.8px;line-height:18px;color:var(--white)}
.btn-solid{position:absolute;left:555px;top:264px;width:90px;height:32px;background:var(--yellow);color:#6a5a10;font-family:"Arimo",sans-serif;font-weight:700;font-size:8.5px;display:flex;align-items:center;justify-content:center}

/* footer */
.site-footer{position:absolute;left:0;top:2207px;width:1200px;height:253px;background:var(--footer)}
.footer-brand{position:absolute;left:235px;top:58px;font-weight:700;font-size:23px;color:#333}
.footer-col{position:absolute;top:66px}
.footer-col h4{font-family:"Arimo",sans-serif;font-weight:400;font-size:8.8px;color:#222;margin-bottom:8px;letter-spacing:.2px}
.footer-col li{list-style:none;font-size:8.4px;line-height:15px;color:#8a8a8a}
.footer-bar{position:absolute;left:0;top:2460px;width:1200px;height:75px;background:var(--footer-bar)}
.copyright{position:absolute;left:0;width:1200px;top:17px;text-align:center;font-family:"Arimo",sans-serif;font-size:7px;color:#222}
.legal{position:absolute;left:240px;width:720px;top:28px;text-align:center;font-family:"Arimo",sans-serif;font-size:6.2px;line-height:10px;color:#9a9a9a}
</style>
</head>
<body>

<header class="site-header">
  <div class="brand">StepTrova</div>
  <div class="topbar">
    <span><svg width="9" height="9" viewBox="0 0 10 10"><path d="M2 1l2 2-1 1.3c.6 1.3 1.4 2.1 2.7 2.7L7 6l2 2-1.3 1.5C4.5 9.3.7 5.5.5 2.3z" fill="#fff"/></svg>(555) 010-2468</span>
    <span><svg width="10" height="10" viewBox="0 0 10 10"><circle cx="5" cy="5" r="4.3" fill="none" stroke="#fff"/><path d="M.7 5h8.6M5 .7c-2 2.5-2 6 0 8.6M5 .7c2 2.5 2 6 0 8.6" fill="none" stroke="#fff" stroke-width=".7"/></svg>español</span>
  </div>
  <div class="social"><i></i><i></i><i></i><i></i><i></i></div>
  <nav class="main-nav">
    <a class="active">HOME</a><a>ABOUT US</a><a>NEWS</a><a>DANCE CLASSES</a><a>DANCE INSTRUCTORS</a><a>DANCE STUDIOS</a>
  </nav>
</header>

<section class="hero">
  <div class="hero-art" role="img" aria-label="Two street dancers leaping against a light backdrop with clouds of coloured ink"></div>
  <h1 class="hero-title">LOREM IPSUM DOLOR<br>CONSECTETUR</h1>
  <div class="hero-rule"></div>
  <p class="hero-sub">Cras vel libero ut lacus eleifend tempor. Phasellus eleifend</p>
  <div class="search">SEARCH FOR DANCE CLASSES NEAR YOU
    <svg width="12" height="12" viewBox="0 0 12 12"><circle cx="5" cy="5" r="3.8" fill="none" stroke="#7b0c7e" stroke-width="1.4"/><path d="M7.8 7.8L11 11" stroke="#7b0c7e" stroke-width="1.5"/></svg>
  </div>
</section>

<h2 class="section-title" style="top:557px">Dance Instructors Near You</h2>
<div class="section-rule" style="top:601px"></div>

<article class="instructor" style="left:234px">
  <div class="avatar" role="img" aria-label="Instructor portrait"></div>
  <h3>Donec a lectus</h3><div class="rule"></div>
  <p>Lorem ipsum dolor sit amet, consectetur adipiscing elit. Nulla lobortis consequat mauris, eget eleifend nunc viverra viverra. Ut ac risus odio. Aliquam pretium purus sed nulla feugiat blandit. Cras vel libero ut lacus eleifend tempor. Phasellus eleifend,</p>
  <div class="divider"></div><a>Read More</a>
</article>
<article class="instructor featured" style="left:422px">
  <div class="avatar" role="img" aria-label="Instructor portrait" style="background:linear-gradient(135deg,#c07a3a,#6a3c1c)"></div>
  <h3>Donec a lectus</h3><div class="rule"></div>
  <p>Lorem ipsum dolor sit amet, consectetur adipiscing elit. Nulla lobortis consequat mauris, eget eleifend nunc viverra viverra. Ut ac risus odio. Aliquam pretium purus sed nulla feugiat blandit. Cras vel libero ut lacus eleifend tempor. Phasellus eleifend,</p>
  <div class="divider"></div><a>Read More</a>
</article>
<article class="instructor" style="left:609px">
  <div class="avatar" role="img" aria-label="Instructor portrait" style="background:linear-gradient(135deg,#6a4a3a,#1e1a1a)"></div>
  <h3>Donec a lectus</h3><div class="rule"></div>
  <p>Lorem ipsum dolor sit amet, consectetur adipiscing elit. Nulla lobortis consequat mauris, eget eleifend nunc viverra viverra. Ut ac risus odio. Aliquam pretium purus sed nulla feugiat blandit. Cras vel libero ut lacus eleifend tempor. Phasellus eleifend,</p>
  <div class="divider"></div><a>Read More</a>
</article>
<article class="instructor" style="left:797px">
  <div class="avatar" role="img" aria-label="Instructor portrait" style="background:linear-gradient(135deg,#cfb48a,#7a6a58)"></div>
  <h3>Donec a lectus</h3><div class="rule"></div>
  <p>Lorem ipsum dolor sit amet, consectetur adipiscing elit. Nulla lobortis consequat mauris, eget eleifend nunc viverra viverra. Ut ac risus odio. Aliquam pretium purus sed nulla feugiat blandit. Cras vel libero ut lacus eleifend tempor. Phasellus eleifend,</p>
  <div class="divider"></div><a>Read More</a>
</article>

<div class="about-art" role="img" aria-label="Group of dancers jumping in a bright dance studio"></div>
<section class="about-panel">
  <h2 class="about-title">ABOUT<br><span>STEPTROVA</span></h2>
  <div class="about-rule"></div>
  <p class="about-text">Lorem ipsum dolor sit amet, consectetur adipiscing elit. Nulla lobortis consequat mauris, eget eleifend nunc viverra viverra. Ut ac risus odio. Aliquam pretium purus sed nulla feugiat blandit. Cras vel libero ut lacus eleifend tempor. Phasellus eleifend, magna non tincidunt accumsan, justo arcu cursus ipsum, non porttitor sapien quam vel magna. Maecenas elit nisl, molestie nec dapibus nec, aliquet a erat. Donec scelerisque lacus a libero suscipit auctor volutpat enim euismod.</p>
  <div class="btn-outline">READ MORE</div>
</section>

<h2 class="section-title" style="top:1424px">Dance Studios</h2>
<div class="section-rule" style="top:1468px"></div>

<article class="studio featured" style="left:234px;top:1499px"><div class="studio-photo" role="img" aria-label="Dancers in a studio class" style="background:linear-gradient(160deg,#8a7aa8,#c45c9a 50%,#5a4a7a)"></div><h3>Lorem ipsum dolo</h3><div class="rule"></div><p>Lorem ipsum dolor sit ame consectetur adipiscing elit. Nulla lobortis consequat mauris, eget eleifend</p></article>
<article class="studio" style="left:484px;top:1499px"><div class="studio-photo" role="img" aria-label="Dancers in a studio class"></div><h3>Lorem ipsum dolo</h3><div class="rule"></div><p>Lorem ipsum dolor sit ame consectetur adipiscing elit. Nulla lobortis consequat mauris, eget eleifend</p></article>
<article class="studio" style="left:734px;top:1499px"><div class="studio-photo" role="img" aria-label="Dancers in a studio class"></div><h3>Lorem ipsum dolo</h3><div class="rule"></div><p>Lorem ipsum dolor sit ame consectetur adipiscing elit. Nulla lobortis consequat mauris, eget eleifend</p></article>
<article class="studio" style="left:234px;top:1630px"><div class="studio-photo" role="img" aria-label="Dancers in a studio class"></div><h3>Lorem ipsum dolo</h3><div class="rule"></div><p>Lorem ipsum dolor sit ame consectetur adipiscing elit. Nulla lobortis consequat mauris, eget eleifend</p></article>
<article class="studio" style="left:484px;top:1630px"><div class="studio-photo" role="img" aria-label="Dancers in a studio class"></div><h3>Lorem ipsum dolo</h3><div class="rule"></div><p>Lorem ipsum dolor sit ame consectetur adipiscing elit. Nulla lobortis consequat mauris, eget eleifend</p></article>
<article class="studio" style="left:734px;top:1630px"><div class="studio-photo" role="img" aria-label="Dancers in a studio class"></div><h3>Lorem ipsum dolo</h3><div class="rule"></div><p>Lorem ipsum dolor sit ame consectetur adipiscing elit. Nulla lobortis consequat mauris, eget eleifend</p></article>

<section class="promo">
  <div class="promo-art" role="img" aria-label="Three hip-hop dancers in motion, tinted blue"></div>
  <p class="promo-kicker">Lorem ipsum dolor sit amet</p>
  <h2 class="promo-title">CONSECTETUR ADIPISCING ELIT</h2>
  <div class="promo-rule"></div>
  <p class="promo-text">Lorem ipsum dolor sit amet, consectetur adipiscing elit. Nulla lobortis consequat mauris,<br>eget eleifend nunc viverra viverra. Ut ac risus odio. Lorem ipsum dolor sit amet, consectetur adipiscing elit. Nulla lobortis consequat<br>mauris, eget eleifend nunc viverra viverra. Ut ac risus odio.</p>
  <div class="btn-solid">READ MORE</div>
</section>

<footer class="site-footer">
  <div class="footer-brand">StepTrova</div>
  <div class="footer-col" style="left:396px"><h4>LOREM IPSUM</h4><ul><li>Lorem ipsum dolor</li><li>Sit amet consectetur</li><li>Adipiscing elit</li><li>Nulla lobortis consequat</li><li>Mauris eget eleifend</li><li>Nunc viverra viverra</li><li>Ut ac risus odio</li></ul></div>
  <div class="footer-col" style="left:527px"><h4>EGET PULVINAR</h4><ul><li>Lorem ipsum</li><li>Dolor sit amet</li><li>Consectetur adipis</li><li>Cing elit Nulla lobortis</li><li>Consequat mauris</li></ul></div>
  <div class="footer-col" style="left:651px"><h4>DONEC PORTTITOR</h4><ul><li>Lorem ipsum dolor</li><li>Sit amet consectetur</li><li>Adipiscing elit</li><li>Nulla lobortis</li><li>Consequat Mauris</li><li>Eget eleifend</li><li>Nunc viverra viverra</li><li>Ut ac risus odio</li><li>Aliquam pretium purus</li></ul></div>
  <div class="footer-col" style="left:777px"><h4>NULLA FEUGIAT</h4><ul><li>Lorem ipsum</li><li>Dolor Sit</li><li>Amet consectetur</li><li>Adipiscing elit</li></ul></div>
  <div class="footer-col" style="left:893px"><h4>PULVINAR</h4><ul><li>Lorem</li><li>Ipsum dolor</li><li>Sit amet</li><li>Consectetur Adipis</li><li>Cing elit</li><li>Nulla lobortis</li><li>Consequat Mauris</li><li>Eget eleifend</li></ul></div>
</footer>
<div class="footer-bar">
  <p class="copyright">Copyright 2017 StepTrova</p>
  <p class="legal">Lorem ipsum dolor sit amet, consectetur adipiscing elit. Nulla lobortis consequat mauris, eget eleifend nunc viverra viverra. Ut ac risus odio. Aliquam pretium purus sed nulla feugiat blandit. Cras vel libero ut lacus eleifend tempor. Phasellus eleifend, magna non tincidunt accumsan, justo arcu cursus ipsum, non porttitor sapien quam vel magna. Maecenas elit nisl, molestie nec dapibus nec, aliquet a erat. Donec scelerisque lacus a libero suscipit auctor volutpat enim euismod. Mauris porta, lacus ut ullamcorper sodales, mauris tortor feugiat purus, nec aliquam neque purus ac metus. Nunc eleifend leo quis nisl hendrerit ultrices. Suspendisse quis feugiat elit. Fusce vitae dolor ac est tincidunt feugiat. Phasellus volutpat dui in sapien malesuada tempus</p>
</div>

</body>
</html>
```